Beauty Packaging Design for small bottle

Design label to have a similar look and feel as other products (as attached for reference). This will be a printed on a gold metallic label, so although the design should be in gold to show us how it will eventually look, the final file will need to have the gold areas in red.

All project information is outline in the attached brief. Please contact us for any questions along the way.

Target Market(s)

Educated, savvy women 30-65 yrs old.

Industry/Entity Type

Hair And Beauty

Font styles to use
Other font styles liked:
• See brief

Requirements
Must have
• See brief
• Color(s): black, gold, white
Nice to have
• purple (CMYK 33/55/0/51)
Should not have
• See brief

```html
<!DOCTYPE html>
<html lang="en">
<head>
<meta charset="utf-8">
<title>Noctera Plus – Label</title>
<link href="https://fonts.googleapis.com/css2?family=Didact+Gothic&family=Montserrat:wght@400&family=Open+Sans:wght@400&family=Playfair+Display:wght@700&family=Playball&display=swap" rel="stylesheet">
<style>
  :root {
    --bg: #a9a9a9;
    --label: #0b0b0b;
    --purple: #6b3d86;
    --white: #ffffff;
    --gold-light: #f3d35a;
    --gold-mid: #d19a2a;
    --gold-dark: #8a5a17;
  }
  html, body {
    margin: 0;
    padding: 0;
    width: 1200px;
    height: 971px;
    overflow: hidden;
    background: var(--bg);
  }
  .canvas {
    position: relative;
    width: 1200px;
    height: 971px;
    background: radial-gradient(ellipse at 50% 45%, #c4c4c4 0%, var(--bg) 70%);
  }
  .label {
    position: absolute;
    left: 280px;
    top: 45px;
    width: 640px;
    height: 880px;
    background: var(--label);
    color: var(--white);
    font-family: "Didact Gothic", sans-serif;
  }
  .rule {
    position: absolute;
    left: 0;
    width: 100%;
    height: 2px;
    background: var(--purple);
  }
  .rule--top { top: 18px; }
  .rule--brand { top: 164px; }
  .rule--info { top: 702px; }
  .rule--volume { top: 818px; }
  .brand {
    position: absolute;
    top: 62px;
    left: 0;
    width: 100%;
    display: flex;
    justify-content: center;
    align-items: center;
    gap: 18px;
  }
  .brand-dot {
    width: 54px;
    height: 54px;
    border-radius: 50%;
    background: var(--white);
  }
  .brand-name {
    font-family: "Montserrat", sans-serif;
    font-weight: 400;
    font-size: 62px;
    letter-spacing: 6px;
    line-height: 1;
    border-bottom: 2px solid var(--white);
    padding-bottom: 8px;
  }
  .ornament {
    position: absolute;
    left: 93px;
    top: 200px;
    width: 455px;
    height: 448px;
    border-radius: 24px;
    background:
      radial-gradient(ellipse 46% 26% at 50% 50%, var(--label) 0%, var(--label) 70%, rgba(11,11,11,0) 100%),
      radial-gradient(ellipse at 50% 50%, rgba(138,90,23,0.35) 0%, rgba(209,154,42,0.6) 60%, rgba(243,211,90,0.75) 100%);
  }
  .product-name {
    position: absolute;
    left: 0;
    width: 100%;
    text-align: center;
  }
  .product-name__main {
    top: 368px;
    font-family: "Playfair Display", serif;
    font-weight: 700;
    font-size: 84px;
    line-height: 1;
    letter-spacing: 1px;
  }
  .product-name__sub {
    top: 452px;
    font-family: "Playball", cursive;
    font-size: 76px;
    line-height: 1;
  }
  .tagline {
    position: absolute;
    top: 656px;
    width: 100%;
    text-align: center;
    font-size: 29px;
    letter-spacing: 0.5px;
  }
  .ingredients {
    position: absolute;
    top: 722px;
    width: 100%;
    text-align: center;
    font-size: 22px;
    line-height: 29px;
  }
  .ingredients p { margin: 0; }
  .volume {
    position: absolute;
    top: 838px;
    width: 100%;
    text-align: center;
    font-family: "Open Sans", sans-serif;
    font-size: 29px;
    line-height: 1;
  }
</style>
</head>
<body>
<div class="canvas">
  <div class="label">
    <div class="rule rule--top"></div>

    <div class="brand">
      <div class="brand-dot"></div>
      <div class="brand-name">LUMERA</div>
    </div>

    <div class="rule rule--brand"></div>

    <div class="ornament" role="img" aria-label="Gold filigree scroll ornament framing the product name"></div>

    <div class="product-name product-name__main">NOCTERA</div>
    <div class="product-name product-name__sub">Plus</div>

    <div class="tagline">Intensive Overnight Moisturizer</div>

    <div class="rule rule--info"></div>

    <div class="ingredients">
      <p>Retinol %2.5 &nbsp;&nbsp;-&nbsp;&nbsp; Hyaluronic Acid</p>
      <p>Aloe Vera, Sunflower Oil, Jojoba Oil, Shea Butter</p>
      <p>Vitamin E &amp; Green Tea</p>
    </div>

    <div class="rule rule--volume"></div>

    <div class="volume">2 fl.oz. / 60 ml</div>
  </div>
</div>
</body>
</html>
```